Plorvan Pte Ltd

I want a creative and stand out web page so when my client search for my web page or google search. The front page is stand out and they know that we are the interior office designer that are searching for . We are commercial office design company. We also have the video to put at our front page for client to see. Natural is the key elements. As we like to carry recycle materials , plant , trees is our key element such as biophilic design
Updates

Hi All,

For my web page, I need minimalist design and creative frontpage.
When my client search for my web page, they straight feel that this is the office design company.
The webpage is special and nature is the key element for the design.
My company logo can be design in the shaped of the letter OO in the webpage.
Below is the sample you can refer.

https://www.mavrelink.example/pin/271950364812057329/

Target Market(s)

Customer searching for office design

Industry/Entity Type

Commerical designer firm- Office interior design & Build company

Number of Pages Required

5+ page

Font styles to use
Other font styles liked:
• Wilmina

Colors
59FF00
82FF00
B8FF75
E3FFCB
F4FFEA
FFC000
F8CF3A
FAE287
FDF2CF
FEFAEE
6B429C
8869AF
B7A5CE
E3DAEB
F3F0F8

Requirements
Must have
• Home, Services,Gallery, Calculator, Testimonials, Contact, Blog
Nice to have
• Natural, creative, minimalist
Should not have
• No black color or blue color

```html
<!DOCTYPE html>
<html lang="en">
<head>
<meta charset="utf-8">
<title>Plorvan Pte Ltd – Office Interior Design</title>
<link href="https://fonts.googleapis.com/css2?family=Poppins:wght@300;400;500;600&display=swap" rel="stylesheet">
<style>
:root{
  --canvas:#f4f2ef;
  --page:#eeebe6;
  --brown:#6b3f16;
  --brown-dark:#4f2d0f;
  --gold:#a8742e;
  --gold-light:#e0b56d;
  --tan:#b49f87;
  --ink:#2e241c;
  --muted:#8a7d70;
  --white:#ffffff;
}
*{box-sizing:border-box;margin:0;padding:0}
html,body{width:1200px;height:3756px;overflow:hidden}
body{background:var(--canvas);font-family:"Poppins",sans-serif;color:var(--ink);position:relative}
.page{position:absolute;left:128px;top:320px;width:944px;height:3300px;background:var(--page);overflow:hidden}
.abs{position:absolute}
.photo{border-radius:14px}
/* nav */
.nav{left:32px;top:24px;width:888px;height:28px;display:flex;align-items:center}
.brand{display:flex;align-items:center;gap:8px;font-weight:600;font-size:15px;color:var(--brown);white-space:nowrap}
.brand-dot{width:14px;height:14px;border-radius:50%;background:var(--brown)}
.nav-links{display:flex;gap:52px;margin-left:150px;font-size:12px;color:var(--muted)}
.nav-links .active{color:var(--brown);font-weight:600;border-bottom:2px solid var(--brown)}
.nav-icons{margin-left:auto;display:flex;gap:10px}
.nav-icon{width:22px;height:22px;border-radius:50%;background:var(--brown);display:flex;align-items:center;justify-content:center}
/* hero */
.hero{left:32px;top:64px;width:888px;height:464px;border-radius:22px;background:linear-gradient(120deg,#8c7a64 0%,#d8d2c6 45%,#b7ab99 70%,#5d5246 100%)}
.hero-card{left:48px;top:80px;width:360px;height:416px;border-radius:18px;background:rgba(78,52,28,.82);padding:22px;color:var(--white)}
.hero-title{font-size:30px;font-weight:600;line-height:1.15}
.hero-title span{color:var(--gold-light)}
.hero-row{display:flex;justify-content:space-between;margin-top:18px;font-size:11px;border-bottom:1px solid rgba(255,255,255,.3);padding-bottom:6px}
.hero-thumbs{display:flex;gap:10px;margin-top:14px}
.hero-thumb{flex:1;height:92px;border-radius:10px;background:linear-gradient(135deg,#a08462,#3f2c1c)}
.hero-text{font-size:10px;line-height:1.6;margin-top:14px;opacity:.85}
.hero-btn{margin-top:18px;display:inline-flex;align-items:center;gap:10px;background:var(--brown-dark);border-radius:20px;padding:6px 18px 6px 6px;font-size:11px}
.hero-btn i{width:24px;height:24px;border-radius:50%;background:var(--white)}
.dots{left:576px;top:500px;display:flex;gap:6px}
.dots b{width:6px;height:6px;border-radius:50%;background:rgba(255,255,255,.6)}
.dots b.on{width:18px;border-radius:3px;background:var(--white)}
.arrows{display:flex;gap:6px}
.arrow{width:26px;height:26px;border-radius:50%;background:var(--white);display:flex;align-items:center;justify-content:center}
.arrow.dark{background:var(--brown)}
/* welcome */
.welcome{left:32px;top:596px;width:560px;font-size:50px;font-weight:400;line-height:1.05;white-space:nowrap}
.welcome span{color:var(--gold)}
.tagline{left:612px;top:606px;width:270px;font-size:13px;color:var(--muted);line-height:1.5}
.body-text{font-size:9.5px;line-height:1.6;color:var(--muted)}
/* video */
.video{left:32px;top:1080px;width:888px;height:328px;border-radius:20px;background:linear-gradient(180deg,#1f1a16,#3b3128 60%,#17130f)}
.play{left:446px;top:1214px;width:60px;height:60px;border-radius:50%;background:var(--white);display:flex;align-items:center;justify-content:center}
/* partner */
.partner-title{left:32px;top:1460px;width:460px;font-size:25px;font-weight:500;line-height:1.3}
.tabs{left:172px;top:1580px;display:flex;flex-direction:column;gap:14px}
.tab{width:160px;height:28px;border-radius:14px;border:1px solid var(--tan);font-size:10px;display:flex;align-items:center;justify-content:center;color:var(--muted)}
.tab.active{background:var(--brown);color:var(--white);border-color:var(--brown)}
/* calculators */
.section-title{font-size:25px;font-weight:500}
.calc{border-radius:18px;padding:30px 26px;color:var(--white)}
.calc-num{font-size:26px;font-weight:300}
.calc-name{font-size:15px;font-weight:600;line-height:1.3;margin-top:8px}
/* blog */
.blog-card{width:200px;top:2820px}
.blog-img{height:130px;border-radius:12px;background:linear-gradient(135deg,#a99680,#5f5040)}
.blog-title{font-size:12px;font-weight:500;line-height:1.35;margin:10px 0 6px}
/* footer */
.footer{left:32px;top:3140px;width:888px;height:148px;border-radius:18px;background:var(--brown);color:var(--white);padding:36px 40px;display:flex;gap:56px}
.footer .brand{color:var(--white)}
.footer .brand-dot{background:var(--white)}
.f-col h4{font-size:12px;font-weight:600;margin-bottom:8px}
.f-col p{font-size:10px;line-height:1.6;opacity:.85}
</style>
</head>
<body>
<div class="page">
  <nav class="abs nav">
    <div class="brand"><span class="brand-dot"></span>Plorvan</div>
    <div class="nav-links"><span class="active">Home</span><span>Portfolio</span><span>Services</span><span>Calculators</span><span>Blog</span></div>
    <div class="nav-icons">
      <span class="nav-icon"><svg width="10" height="10" viewBox="0 0 10 10"><circle cx="4.3" cy="4.3" r="3" fill="none" stroke="#fff" stroke-width="1.3"/><line x1="6.5" y1="6.5" x2="9" y2="9" stroke="#fff" stroke-width="1.3"/></svg></span>
      <span class="nav-icon"><svg width="10" height="10" viewBox="0 0 10 10"><path d="M2 1.5l2 2-1 1.2a6 6 0 002.3 2.3l1.2-1 2 2-1 1.5C4.5 9.5.5 5.5 1 2.5z" fill="#fff"/></svg></span>
    </div>
  </nav>

  <div class="abs hero" role="img" aria-label="Photo of a bright office interior with a staircase, plants and workstations"></div>
  <div class="abs hero-card">
    <div class="hero-title">Norvik Freight<br>Kuala <span>Lumpur</span></div>
    <div class="hero-row"><span>Detail</span><span>Full Fitout</span></div>
    <div class="hero-thumbs">
      <div class="hero-thumb" role="img" aria-label="Photo of the office reception"></div>
      <div class="hero-thumb" role="img" aria-label="Photo of the meeting room"></div>
    </div>
    <p class="hero-text">Location: Menara Timur Tower, Kuala Lumpur<br>Floor Space: 18,000 sqft</p>
    <span class="hero-btn"><i></i>View detail</span>
  </div>
  <div class="abs dots"><b class="on"></b><b></b><b></b><b></b></div>
  <div class="abs arrows" style="left:846px;top:494px">
    <span class="arrow"><svg width="8" height="8" viewBox="0 0 8 8"><path d="M5 1L2 4l3 3" fill="none" stroke="#6b3f16" stroke-width="1.4"/></svg></span>
    <span class="arrow"><svg width="8" height="8" viewBox="0 0 8 8"><path d="M3 1l3 3-3 3" fill="none" stroke="#6b3f16" stroke-width="1.4"/></svg></span>
  </div>

  <h1 class="abs welcome">Welcome to <span>Plorvan</span><br>Singapore</h1>
  <p class="abs tagline">A Singapore Reputable Commercial Interior Design &amp; Office Renovation Company</p>

  <div class="abs photo" style="left:32px;top:720px;width:372px;height:308px;background:linear-gradient(135deg,#c9bcab,#6f5e4c)" role="img" aria-label="Photo of a team meeting around an office table"></div>
  <div class="abs photo" style="left:424px;top:720px;width:496px;height:150px;background:linear-gradient(135deg,#e2d9cd,#9a8b79)" role="img" aria-label="Photo of hands sketching an office floor plan"></div>
  <p class="abs body-text" style="left:424px;top:886px;width:200px">Our studio plans each office around the way your team works, bringing daylight, timber and greenery into every space we build.</p>
  <p class="abs body-text" style="left:424px;top:960px;width:200px">From first sketch to final handover, one team manages design, approvals and build.</p>
  <p class="abs body-text" style="left:640px;top:886px;width:260px">We reuse materials wherever we can and add living plants for calmer, healthier workplaces.</p>
  <div class="abs photo" style="left:640px;top:930px;width:280px;height:98px;background:linear-gradient(135deg,#b8aa98,#5a4a3a)" role="img" aria-label="Photo of a designer reviewing material samples"></div>

  <div class="abs video" role="img" aria-label="Video still of a dark office corridor with ring lights"></div>
  <div class="abs play"><svg width="20" height="20" viewBox="0 0 20 20"><path d="M6 3l11 7-11 7z" fill="#2e241c"/></svg></div>

  <h2 class="abs partner-title">Your One-Stop Office Renovation &amp; Interior Design Partner</h2>
  <p class="abs body-text" style="left:540px;top:1462px;width:300px">We guide you from start to end of the journey. To ensure that the project and our well organised plan come forward, a dedicated project manager will be assigned. We build your vision with care.</p>
  <div class="abs tabs">
    <span class="tab">Interior</span>
    <span class="tab active">Renovation</span>
    <span class="tab">Space planning</span>
    <span class="tab">Space partitioning</span>
    <span class="tab">See all</span>
  </div>
  <div class="abs photo" style="left:392px;top:1580px;width:528px;height:262px;background:linear-gradient(120deg,#efe9e0,#c4b39d 55%,#7d6a56)" role="img" aria-label="Photo of a renovated office with rows of desks and black chairs"></div>
  <div class="abs arrows" style="left:850px;top:1806px">
    <span class="arrow"><svg width="8" height="8" viewBox="0 0 8 8"><path d="M5 1L2 4l3 3" fill="none" stroke="#6b3f16" stroke-width="1.4"/></svg></span>
    <span class="arrow"><svg width="8" height="8" viewBox="0 0 8 8"><path d="M3 1l3 3-3 3" fill="none" stroke="#6b3f16" stroke-width="1.4"/></svg></span>
  </div>

  <h2 class="abs section-title" style="left:32px;top:1900px">Our calculators</h2>
  <div class="abs calc" style="left:32px;top:1980px;width:288px;height:200px;background:var(--tan);color:var(--ink)">
    <div class="calc-num">01</div><div class="calc-name">Office Floor Space Calculator</div>
  </div>
  <div class="abs calc" style="left:328px;top:1948px;width:296px;height:252px;background:var(--brown)">
    <div class="calc-num">02</div><div class="calc-name">Renovation Budget Calculator</div>
    <p style="font-size:10px;line-height:1.6;margin-top:10px;opacity:.85">Plan your budget before you start. Enter your floor area and finish level to see a quick estimate.</p>
    <span class="arrow" style="position:absolute;right:20px;bottom:20px"><svg width="8" height="8" viewBox="0 0 8 8"><path d="M3 1l3 3-3 3" fill="none" stroke="#6b3f16" stroke-width="1.4"/></svg></span>
  </div>
  <div class="abs calc" style="left:632px;top:1980px;width:288px;height:200px;background:var(--tan);color:var(--ink)">
    <div class="calc-num">03</div><div class="calc-name">Project Timeline Calculator</div>
  </div>

  <h2 class="abs section-title" style="left:32px;top:2240px">Project Gallery</h2>
  <p class="abs body-text" style="left:32px;top:2284px;width:180px">Explore our work. Let our designs speak for themselves.</p>
  <div class="abs photo" style="left:252px;top:2230px;width:212px;height:140px;background:linear-gradient(135deg,#b9ab98,#4f4135)" role="img" aria-label="Photo of an open plan office"></div>
  <div class="abs photo" style="left:252px;top:2384px;width:212px;height:200px;background:linear-gradient(135deg,#8d7660,#2f241a)" role="img" aria-label="Photo of a dining area with pendant lights"></div>
  <div class="abs photo" style="left:476px;top:2230px;width:212px;height:280px;background:linear-gradient(180deg,#d8c29c,#a07a4c 60%,#5c4630)" role="img" aria-label="Photo of a warm wood-panelled lobby"></div>
  <div class="abs photo" style="left:476px;top:2522px;width:212px;height:90px;background:linear-gradient(135deg,#c6b7a4,#77634f)" role="img" aria-label="Photo of a meeting table"></div>
  <div class="abs photo" style="left:700px;top:2230px;width:220px;height:150px;background:linear-gradient(135deg,#e6ddcf,#a4957f)" role="img" aria-label="Photo of a bright pantry"></div>
  <div class="abs photo" style="left:700px;top:2392px;width:220px;height:220px;background:linear-gradient(135deg,#d99b4c,#8a5a2a)" role="img" aria-label="Photo of a lounge with orange accent wall"></div>

  <h2 class="abs section-title" style="left:32px;top:2728px">Blog</h2>
  <p class="abs body-text" style="left:32px;top:2772px;width:240px">Our team of design experts will inspire you with their innovative ideas, tips and tricks for transforming your office.</p>
  <div class="abs arrows" style="left:862px;top:2760px">
    <span class="arrow"><svg width="8" height="8" viewBox="0 0 8 8"><path d="M5 1L2 4l3 3" fill="none" stroke="#6b3f16" stroke-width="1.4"/></svg></span>
    <span class="arrow dark"><svg width="8" height="8" viewBox="0 0 8 8"><path d="M3 1l3 3-3 3" fill="none" stroke="#fff" stroke-width="1.4"/></svg></span>
  </div>
  <article class="abs blog-card" style="left:32px"><div class="blog-img" role="img" aria-label="Photo of a minimalist office desk"></div><h3 class="blog-title">A must-have for a minimalist office design in Singapore</h3><p class="body-text">Clean lines and calm tones for focus.</p></article>
  <article class="abs blog-card" style="left:248px"><div class="blog-img" role="img" aria-label="Photo of an office with indoor plants"></div><h3 class="blog-title">The Do's and Don'ts in creating a biophilic office</h3><p class="body-text">Bring nature indoors the right way.</p></article>
  <article class="abs blog-card" style="left:464px"><div class="blog-img" role="img" aria-label="Photo of a collaborative work area"></div><h3 class="blog-title">Office interior design tips to improve workplace wellbeing</h3><p class="body-text">Small changes, happier teams.</p></article>
  <article class="abs blog-card" style="left:680px"><div class="blog-img" role="img" aria-label="Photo of a modern reception"></div><h3 class="blog-title">7 graphic design trends to bring into your office space in 2023</h3><p class="body-text">Fresh ideas for brand walls.</p></article>
  <article class="abs blog-card" style="left:896px"><div class="blog-img" role="img" aria-label="Photo of an office pantry"></div><h3 class="blog-title">The Do's and Don'ts of a cosy pantry</h3><p class="body-text">Spaces to pause and share.</p></article>

  <footer class="abs footer">
    <div class="brand"><span class="brand-dot"></span>Plorvan Pte Ltd</div>
    <div class="f-col"><h4>Office Address</h4><p>21 Keller Road #04-12<br>Singapore 408650</p></div>
    <div class="f-col"><h4>Contact Person</h4><p>Dana Mirel</p></div>
    <div class="f-col"><h4>Phone</h4><p>+65 6123 4870</p></div>
    <div class="f-col"><h4>Mail</h4><p>hello@plorvan.example</p></div>
  </footer>
</div>
</body>
</html>
```